Bold Creative Business Card for Digital Marketing Company (Contest)

NOTICE TO DESIGNERS: We understand this is how you make your living. Our commitment to you is to give you awesome and rapid feedback. If we don't think you are on the right track or have a chance of winning we will let you know right away so you don't have to focus your time with us and can continue to get work.

We respect the crowdsource community greatly. We have launched hundreds of crowdsource projects and will make this a great experience for you if you choose to participate (we hope you will!)

--------------
Brief
-------------

We are a cutting edge digital marketing company and we need a new, bold and creative business card designed to reflect who we are and what we do. We want our brand to stand out and be noticed.

The name of our company is: Tundrel Web Marketing

Definition of Tundrel:

a. a person pursuing rebellious, even potentially disruptive, policies or ideas:

b. a lone dissenter, as an intellectual, an artist, or a politician, who takes an independent stand apart from his or her associates

c. unorthodox, unconventional, nonconformist

Our businesses is helping small to medium size businesses with their online marketing using bold and creative outside the box strategies that get results.

We are an industry leader and need our business cards to stand out when we hand them out to people, and to be amazing so we stand out and "lead the pack"!

Our current website: http://www.tundrelwebmarketing.example

We are rebranding our site to reflect the new logo we just got but you will at least have an idea of who we are and what we do.

Colors We Want: We would like to see burnt Orange, Dark Blue, Gray and/or Black.

We need a front and back designed!

Be creative! Even to the point of creative-shaped business cards. Think outside the box. Let nothing stop your imagination! At the very least, we know that we want business cards that are not the US Standard 2"x3.5"... but rather the wider 3.35"x2.17" (European Standard) with rounded corners if you want to stick with a rectangular shape.

On the front we need:

Our Logo
Place for a name ie Dale Voskuij
Place for our phone number (505) 555 - 7680
Place for email name@tundrelwebmarketing.example
Place for our website www.TundrelWebMarketing.example

Optional... Place for a headshot photo of the person who the business card will be used for

On the back we need:

The wording... FREE VIDEO SERIES! "9 Quick Moves To Grow Your Company This Week!" www.TundrelWebMarketing.example/SmartIdeas

We are excited to see what you come up with.

Thank you for your interests and for participating in this contest!
Updates

Hi everyone! Thanks for all your submissions. However, we feel that most of you are "missing" what we're looking for. Almost all of the designs that have come in are what we would call "standard", "generic", or "typical". We are looking for something creative, different, attention-getting, a business card that would stand out amongst a stack of other business cards. I've shot this video: http://clipvault.example/t/qPzTbw4hYcs Please take the time to review it. Let us know if you have questions. Thanks!

Target Market(s)

Our target market is small to medium sized business owners who need help with their online marketing.

Industry/Entity Type

Marketing

Font styles to use
Sans Serif

Colors
0355a3
85acd3
f78f20
f37022
faa54b
f68d4d

Requirements
Must have
• On the front we need:

Our Logo

Be CREATIVE! INTERESTING!

On the back we need:

Use the colors from our logo!
Nice to have
• Optional... Place for a headshot photo of the person who the business card will be used for.
Should not have
• Boring, "traditional" look and feel. We want and need to stand out!

```html
<!DOCTYPE html>
<html lang="en">
<head>
<meta charset="utf-8">
<title>Tundrel Web Marketing – Business Card</title>
<link rel="stylesheet" href="https://fonts.googleapis.com/css2?family=Lato:wght@400;700&display=swap">
<style>
  :root {
    --backdrop: #2a2a2a;
    --card-black: #070707;
    --burnt-orange: #f37022;
    --orange: #f78f20;
    --light-orange: #faa54b;
    --blue: #0355a3;
    --white: #ffffff;
  }
  * { box-sizing: border-box; margin: 0; padding: 0; }
  html, body {
    width: 1200px; height: 900px; overflow: hidden;
    background: var(--backdrop);
    font-family: "Lato", sans-serif;
  }
  .canvas { position: relative; width: 1200px; height: 900px; }

  .card {
    position: absolute;
    width: 560px; height: 363px;
    border-radius: 22px;
    background: var(--card-black);
    overflow: hidden;
    box-shadow: 0 14px 30px rgba(0,0,0,0.55);
  }
  .card--back { left: 50px; top: 80px; }
  .card--front { left: 590px; top: 457px; }

  .brand {
    display: flex; align-items: center; gap: 12px;
    font-weight: 700; color: var(--white);
    letter-spacing: 0.04em;
  }
  .brand__mark { width: 22px; height: 22px; background: var(--burnt-orange); flex: none; }

  /* Back */
  .card--back .brand {
    position: absolute; left: 0; right: 0; top: 96px;
    justify-content: center; font-size: 30px;
  }
  .offer {
    position: absolute; left: 0; right: 0; top: 180px;
    text-align: center; font-weight: 700;
  }
  .offer__kicker {
    color: var(--white); font-size: 18px; letter-spacing: 0.08em;
  }
  .offer__headline { color: var(--orange); font-size: 20px; margin-top: 10px; }
  .offer__link { color: var(--orange); font-size: 18px; margin-top: 8px; }
  .offer__link span { color: var(--light-orange); }

  /* Front */
  .card--front .brand {
    position: absolute; right: 34px; top: 38px; font-size: 24px;
  }
  .name-band {
    position: absolute; left: 0; right: 0; top: 110px; height: 92px;
    background: linear-gradient(90deg, var(--burnt-orange), var(--light-orange) 45%, var(--orange) 80%, var(--burnt-orange));
  }
  .headshot {
    position: absolute; left: 40px; top: 86px;
    width: 104px; height: 104px;
    border: 4px solid #d9d9d9; border-radius: 6px;
    background: linear-gradient(180deg, #7fa9d6, #c8d2dc 60%, #8d8f86);
  }
  .person {
    position: absolute; right: 34px; top: 140px; text-align: right;
    color: var(--white); font-weight: 700;
  }
  .person__name { font-size: 24px; }
  .person__title { font-size: 16px; }
  .contact {
    position: absolute; left: 40px; top: 222px;
    color: var(--orange); font-weight: 700; font-size: 17px; line-height: 1.45;
  }
  .accent-line {
    position: absolute; left: 0; right: 0; top: 318px; height: 3px; background: var(--blue);
  }
  .foot-band {
    position: absolute; left: 0; right: 0; top: 324px; bottom: 0;
    background: linear-gradient(90deg, var(--burnt-orange), var(--orange));
  }
</style>
</head>
<body>
<main class="canvas">

  <section class="card card--back" aria-label="Card back">
    <div class="brand"><span class="brand__mark"></span>Tundrel Web Marketing</div>
    <div class="offer">
      <p class="offer__kicker">FREE VIDEO SERIES!</p>
      <p class="offer__headline">"9 Quick Moves To Grow Your Company This Week!"</p>
      <p class="offer__link">www.TundrelWebMarketing.example/<span>SmartIdeas</span></p>
    </div>
  </section>

  <section class="card card--front" aria-label="Card front">
    <div class="brand"><span class="brand__mark"></span>Tundrel Web Marketing</div>
    <div class="name-band"></div>
    <div class="headshot" role="img" aria-label="Headshot photo of the cardholder"></div>
    <div class="person">
      <p class="person__name">Dale Voskuij</p>
      <p class="person__title">Director</p>
    </div>
    <div class="contact">
      <p class="contact__phone">(505) 555 - 7680</p>
      <p>@tundrelwebmarketing.example</p>
      <p>www.TundrelWebMarketing.example</p>
    </div>
    <div class="accent-line"></div>
    <div class="foot-band"></div>
  </section>

</main>
</body>
</html>
```